Need sign/billboard help

I need somone to take my logo and turn it into a sign.
Needs to have: Bright Paws
Hound Play Lodge LLC
319-555-0187
Daycare - Boarding - Learning
Colors to use are in the pictures i included, however feel free to use different shades of gray. i Don't necessary want to background to be one solid color.
Also this sing will be a rectangle (4'x8')
Industry/Entity Type
Daycare
Look and feel
Each slider illustrates characteristics of the customer's brand and the style your logo design should communicate.

```html
<!DOCTYPE html>
<html lang="en">
<head>
<meta charset="UTF-8">
<title>Bright Paws – Hound Play Lodge Sign</title>
<link rel="stylesheet" href="https://fonts.googleapis.com/css2?family=Open+Sans:ital,wght@0,600;0,700;1,600&display=swap">
<style>
  :root {
    --lime: #9bcb29;
    --slate: #666666;
    --ink: #0b0b0b;
    --paper: #ffffff;
    --light: #f4f4f4;
  }
  * { box-sizing: border-box; margin: 0; padding: 0; }
  html, body {
    width: 1033px;
    height: 1200px;
    overflow: hidden;
    background: var(--paper);
    font-family: "Open Sans", Arial, sans-serif;
  }
  .sign {
    position: absolute;
    left: 101px;
    top: 116px;
    width: 831px;
  }
  .sign-face {
    display: flex;
    height: 346px;
  }
  .brand-panel {
    position: relative;
    width: 630px;
    background: var(--lime);
  }
  .brand-mark {
    position: absolute;
    left: 96px;
    top: 118px;
    display: flex;
    align-items: center;
    gap: 22px;
  }
  .brand-dot {
    width: 70px;
    height: 70px;
    border-radius: 50%;
    background: var(--ink);
  }
  .brand-name {
    font-weight: 700;
    font-size: 62px;
    line-height: 1;
    letter-spacing: 1px;
    color: var(--ink);
    text-transform: uppercase;
  }
  .brand-tagline {
    position: absolute;
    left: 64px;
    top: 276px;
    font-weight: 600;
    font-style: italic;
    font-size: 26px;
    letter-spacing: 2px;
    color: var(--ink);
    text-transform: uppercase;
  }
  .services-panel {
    width: 201px;
    background: linear-gradient(180deg, #6d6d6d 0%, var(--slate) 55%, #5c5c5c 100%);
    padding: 65px 0 0 34px;
  }
  .service {
    font-weight: 600;
    font-size: 26px;
    line-height: 58px;
    color: var(--light);
    text-transform: uppercase;
    letter-spacing: 0.5px;
  }
  .phone-band {
    margin-top: 13px;
    height: 56px;
    background: var(--ink);
    display: flex;
    align-items: center;
    justify-content: center;
  }
  .phone-number {
    font-weight: 600;
    font-size: 40px;
    line-height: 1;
    color: var(--lime);
    letter-spacing: 0.5px;
    margin-right: 84px;
  }
</style>
</head>
<body>
  <section class="sign">
    <div class="sign-face">
      <div class="brand-panel">
        <div class="brand-mark">
          <span class="brand-dot"></span>
          <span class="brand-name">Bright Paws</span>
        </div>
        <p class="brand-tagline">Hound Play Lodge LLC</p>
      </div>
      <div class="services-panel">
        <p class="service">Daycare</p>
        <p class="service">Boarding</p>
        <p class="service">Learning</p>
      </div>
    </div>
    <div class="phone-band">
      <p class="phone-number">319-555-0187</p>
    </div>
  </section>
</body>
</html>
```